Pelling Home Efficiency

Id like for my business card to be very bold and professional. Incorporating the business logo, the main services offered, and my contact info. Services are spray foam, insulation, new construction, retrofit, weatherization.

When opening this project art huddle was not able to upload my new logo that I picked from another recent art huddle project. Does anyone know how i could upload my logo onto the page for design of the business cards?

Target Market(s)

Building owners, contractors

Industry/Entity Type

Building Insulation and performance improvements

Contact Information for Business Card

Owner, Email marcus@pellinghomeefficiency.com Phone number 555-204-6817

Colors
0054AA
0677BA
7BADD7
CADEEF
E8F1F8
F0912C
F2A743
F7CA91
FBE8D2
FDF5EE

Requirements
Must have
• Services- spray foam, cellulose, mineral wool, fiberglass, air sealing, new construction, retrofit, weatherization, energy saving assesments

```html
<!DOCTYPE html>
<html lang="en">
<head>
<meta charset="utf-8">
<title>Pelling Home Efficiency – Business Card</title>
<link href="https://fonts.googleapis.com/css2?family=Roboto:wght@400;500;700;900&display=swap" rel="stylesheet">
<style>
  :root{
    --page:#2b2b2d;
    --card:#151b35;
    --orange:#e8730f;
    --blue:#4fb0e3;
    --white:#ffffff;
    --rule:#d8dde8;
  }
  *{box-sizing:border-box;margin:0;padding:0}
  html,body{width:1200px;height:875px;overflow:hidden}
  body{background:var(--page);font-family:"Roboto",Arial,sans-serif;color:var(--white);position:relative}
  .card{position:absolute;width:560px;height:320px;background:var(--card);border-radius:22px;overflow:hidden}
  .card--front{left:50px;top:80px}
  .card--back{left:590px;top:470px}

  .brand{display:flex;align-items:center;gap:10px}
  .brand__mark{width:22px;height:22px;background:var(--orange);flex:none}
  .brand__name{font-weight:900;color:var(--orange);text-transform:uppercase;line-height:1}
  .brand__rule{height:5px;background:var(--blue);margin-top:8px}

  .card--front .brand-block{position:absolute;left:70px;top:50px;width:420px}
  .card--front .brand__name{font-size:31px;letter-spacing:.5px}

  .services{position:absolute;left:0;right:0;top:140px;text-align:center}
  .services__title{color:var(--blue);font-weight:500;font-size:24px;letter-spacing:1px;margin-bottom:14px}
  .services__line{font-size:17px;line-height:30px}
  .services__line span::before{content:"•";color:var(--orange);margin:0 7px}

  .card--back .brand-block{position:absolute;right:36px;top:38px;width:300px}
  .card--back .brand__name{font-size:21px}
  .divider{position:absolute;left:36px;right:36px;top:138px;height:1px;background:var(--rule)}
  .person{position:absolute;left:36px;top:160px;padding-left:16px;border-left:7px solid var(--orange)}
  .person__name{color:var(--blue);font-weight:500;font-size:25px}
  .person__role{font-size:15px;margin-top:2px}
  .divider--short{top:228px;right:300px}
  .contacts{position:absolute;left:36px;top:240px;list-style:none;font-size:14px}
  .contacts li{display:flex;align-items:center;gap:10px;height:22px}
  .contacts svg{width:15px;height:15px;fill:var(--orange);flex:none}
  .address{position:absolute;right:36px;top:170px;text-align:right;font-size:14px;line-height:22px}
  .stripe{position:absolute;left:0;right:0;bottom:0;height:7px;display:flex}
  .stripe__blue{flex:3;background:var(--blue)}
  .stripe__orange{flex:1;background:var(--orange)}
</style>
</head>
<body>
  <section class="card card--front">
    <div class="brand-block">
      <div class="brand"><span class="brand__mark"></span><span class="brand__name">Pelling Home Efficiency</span></div>
      <div class="brand__rule"></div>
    </div>
    <div class="services">
      <h2 class="services__title">SERVICES</h2>
      <p class="services__line"><span>Spray foam</span><span>Cellulose</span><span>Mineral wool,</span><span>Fiberglass</span></p>
      <p class="services__line"><span>Air sealing</span><span>New construction</span><span>Retrofit</span><span>Weatherization</span></p>
      <p class="services__line"><span>Energy saving</span><span>Assesments</span></p>
    </div>
  </section>

  <section class="card card--back">
    <div class="brand-block">
      <div class="brand"><span class="brand__mark"></span><span class="brand__name">Pelling Home Efficiency</span></div>
      <div class="brand__rule"></div>
    </div>
    <div class="divider"></div>
    <div class="person">
      <h1 class="person__name">Daniel Rowe</h1>
      <p class="person__role">Owner</p>
    </div>
    <div class="divider divider--short"></div>
    <ul class="contacts">
      <li><svg viewBox="0 0 24 24"><path d="M6.6 10.8a15.1 15.1 0 0 0 6.6 6.6l2.2-2.2c.3-.3.7-.4 1-.2 1.1.4 2.3.6 3.6.6.6 0 1 .4 1 1V20c0 .6-.4 1-1 1A17 17 0 0 1 3 4c0-.6.4-1 1-1h3.5c.6 0 1 .4 1 1 0 1.3.2 2.5.6 3.6.1.3 0 .7-.2 1z"/></svg>555-204-6817</li>
      <li><svg viewBox="0 0 24 24"><path d="M2 5h20v14H2zm2 2v.5l8 5 8-5V7l-8 5z"/></svg>marcus@pellinghomeefficiency.com</li>
      <li><svg viewBox="0 0 24 24"><path d="M12 2a10 10 0 1 0 0 20 10 10 0 0 0 0-20zm6.9 6h-3a15 15 0 0 0-1.3-3.8A8 8 0 0 1 18.9 8zM12 4c.8 1.2 1.5 2.5 1.9 4h-3.8c.4-1.5 1.1-2.8 1.9-4zM4.3 14a8 8 0 0 1 0-4h3.4a16 16 0 0 0 0 4zm.8 2h3a15 15 0 0 0 1.3 3.8A8 8 0 0 1 5.1 16zm3-8h-3a8 8 0 0 1 4.3-3.8A15 15 0 0 0 8.1 8zM12 20c-.8-1.2-1.5-2.5-1.9-4h3.8c-.4 1.5-1.1 2.8-1.9 4zm2.3-6H9.7a14 14 0 0 1 0-4h4.6a14 14 0 0 1 0 4zm.3 5.8a15 15 0 0 0 1.3-3.8h3a8 8 0 0 1-4.3 3.8zm1.7-5.8a16 16 0 0 0 0-4h3.4a8 8 0 0 1 0 4z"/></svg>www.pellinghomeefficiency.com</li>
    </ul>
    <p class="address">421, Address line goes here<br>45452, Country name</p>
    <div class="stripe"><span class="stripe__blue"></span><span class="stripe__orange"></span></div>
  </section>
</body>
</html>
```